Photography Studio Prep Guide Design Needed

I have a prep guide I send to all parents who book a session - It is outdated and ugly. I want a gorgeous, clean, modern upscale look for the brochure I send.

I already have the text and can provide photos for the final design. I want the cover to be clean and upscale and modern, with a happy feel.

Target Market(s)

My clients for an upscale Newborn Photography Studio

Requirements
Must have
• space for my photos, an upscale clean feel
Nice to have
• I love color, but don't want the brochure to look busy. I love cream, white, pale pink.

```html
<!DOCTYPE html>
<html lang="en">
<head>
<meta charset="utf-8">
<title>Newborn Session Prep Guide</title>
<link href="https://fonts.googleapis.com/css2?family=Yanone+Kaffeesatz:wght@200;300&family=Parisienne&family=Open+Sans:wght@400;700&display=swap" rel="stylesheet">
<style>
:root{
  --backdrop:#8c8c8c;
  --cover-beige:#cdc1b1;
  --page-beige:#dbcfbf;
  --ink:#7b7069;
  --ink-soft:#8f857c;
  --white:#ffffff;
  --coral:#e9968a;
  --coral-deep:#e08a7d;
}
*{margin:0;padding:0;box-sizing:border-box}
html,body{width:772px;height:1200px;overflow:hidden}
body{background:var(--backdrop);font-family:"Open Sans",sans-serif;color:var(--ink);position:relative}
.spread{position:absolute;left:93px;width:587px;height:366px;display:flex;box-shadow:0 2px 8px rgba(0,0,0,.25)}
.spread--cover{top:25px}
.spread--instructions{top:405px}
.spread--studio{top:783px}
.page{position:relative;width:293.5px;height:100%;overflow:hidden}
.page--cover-back{background:var(--cover-beige)}
.page--beige{background:var(--page-beige)}
.page--coral{background:var(--coral)}
.photo{position:absolute}
.photo--round{border-radius:50%}
.studio-mark{position:absolute;display:flex;align-items:center;justify-content:center;text-align:center;
  font-family:"Open Sans",sans-serif;font-weight:400;color:var(--white);letter-spacing:.08em;text-transform:uppercase;line-height:1.3}
.studio-mark--disc{border-radius:50%;background:var(--cover-beige)}
.cover-title{position:absolute;left:112px;font-family:"Yanone Kaffeesatz",sans-serif;font-weight:200;color:var(--white);font-size:25px;letter-spacing:.04em;line-height:1;white-space:nowrap}
.cover-rule{position:absolute;left:112px;top:288px;width:181.5px;height:1px;background:var(--white)}
.script-title{font-family:"Parisienne",cursive;color:var(--ink-soft);text-align:center;line-height:1.25}
.lead{font-family:"Yanone Kaffeesatz",sans-serif;font-weight:200;text-transform:uppercase;text-align:center;font-size:9.5px;letter-spacing:.05em;line-height:1.55;color:var(--ink);white-space:nowrap}
.section{position:absolute}
.section-head{font-family:"Yanone Kaffeesatz",sans-serif;font-weight:300;text-transform:uppercase;font-size:13px;letter-spacing:.06em;display:flex;align-items:center;gap:6px;margin-bottom:4px;line-height:1}
.num{display:inline-flex;width:10px;height:10px;border-radius:50%;background:var(--ink);color:var(--page-beige);font-family:"Open Sans",sans-serif;font-size:6px;font-weight:700;align-items:center;justify-content:center}
.num--small{width:7px;height:7px;font-size:4px;vertical-align:middle}
.cols{display:grid;grid-template-columns:1fr 1fr;column-gap:10px}
.body{font-size:4.3px;line-height:1.5;text-align:justify;color:var(--ink)}
.body b{font-weight:700}
.page--coral .body{color:#fff3ef}
.page--coral .num{background:var(--white);color:var(--coral)}
</style>
</head>
<body>

<section class="spread spread--cover">
  <div class="page page--cover-back">
    <div class="photo photo--round" role="img" aria-label="Round photo of a sleeping newborn in a purple wrap surrounded by purple and pink flowers"
      style="left:85px;top:77px;width:121px;height:121px;background:radial-gradient(circle,#c9a3c2 0%,#8e4a84 40%,#6a2a5e 75%,#4e1c45 100%)"></div>
    <div class="studio-mark" style="left:96px;top:256px;width:100px;height:40px;font-size:6px">Willow Nest<br>Studio</div>
  </div>
  <div class="page">
    <div class="photo" role="img" aria-label="Photo of a sleeping newborn in a pale blue knit bonnet and wrap on a cream fur rug"
      style="inset:0;background:radial-gradient(ellipse 60% 55% at 62% 48%,#ebbfa4 0%,#e2c3ab 30%,#d4bda6 55%,#b9a088 85%,#a58b73 100%)"></div>
    <div class="studio-mark studio-mark--disc" style="left:32px;top:17px;width:77px;height:77px;font-size:6px">Willow Nest<br>Studio</div>
    <div class="cover-title" style="top:262px">NEWBORN SESSION</div>
    <div class="cover-rule"></div>
    <div class="cover-title" style="top:294px">PREP GUIDE</div>
  </div>
</section>

<section class="spread spread--instructions">
  <div class="page page--beige">
    <div class="section" style="left:20px;top:48px;width:254px">
      <div class="script-title" style="font-size:18px">Parent<br>Instructions &amp; Preparations</div>
      <div class="lead" style="margin-top:14px">Congratulations on expecting a baby!<br>Here are my instructions to ensure<br>a successful newborn photography session<br>please follow these instructions as closely as possible</div>
    </div>
    <div class="section" style="left:35px;top:212px;width:228px">
      <div class="section-head"><span class="num">1</span>Nursing</div>
      <div class="cols">
        <p class="body">If you are nursing, please avoid eating anything spicy (hot sauce, peppers, curry, etc.) that might upset baby's tummy for 24 hours before your scheduled session. Please also avoid caffeine or coffee before your session. I know this is hard but baby will be wired if you have caffeine. If you notice baby has</p>
        <p class="body">a lot of gas after feedings please check with your pediatrician and bring gas drops with you. The most common reason a baby will not settle for a session is gas pressure and discomfort.</p>
      </div>
    </div>
    <div class="section" style="left:35px;top:282px;width:228px">
      <div class="section-head"><span class="num">2</span>Feeding</div>
      <div class="cols">
        <p class="body">Feed the baby as much as possible in the 24 hours preceding your session. This will help keep baby full and sleepy through the session. Feed baby two to three hours before your session and again right when you arrive. This feeding is planned in your session time and it's not rushed.<br><b>Please bring an extra bottle of formula or breast-</b></p>
        <p class="body"><b>milk to the session if possible. Sometimes a small amount of milk in a bottle can quickly soothe a baby back to sleep without requiring a full feeding.</b> I will respect your wishes if you choose not to use a bottle, but please understand we may have to pass on some poses if baby will not settle.</p>
      </div>
    </div>
  </div>
  <div class="page page--beige">
    <div class="photo" role="img" aria-label="Photo of a sleeping newborn with a blush flower headband and soft feather wings on white lace"
      style="left:0;top:0;width:100%;height:180px;background:radial-gradient(ellipse 55% 60% at 48% 50%,#efc9bc 0%,#f0d9cf 35%,#f4ebe5 70%,#faf6f2 100%)"></div>
    <div class="section" style="left:36px;top:196px;width:228px">
      <div class="section-head"><span class="num">3</span>Keep baby awake</div>
      <div class="cols">
        <p class="body">Interact with, and keep baby awake for 2 hours preceding your appointment to make sure they are nice and sleepy for their session. A great way to do this is by giving baby a bath, which will get them nice and clean and keep them awake.</p>
        <p class="body">Also, keeping baby naked, in a diaper only, is a good way to keep them awake and alert. This step is extremely important, otherwise it can take a long time to get baby to sleep, and we will have less time for photos.</p>
      </div>
    </div>
    <div class="section" style="left:36px;top:256px;width:228px">
      <div class="section-head"><span class="num">4</span>Clothes</div>
      <div class="cols">
        <p class="body">Please dress baby in a simple loose sleeper we can just unsnap when you arrive. We want to keep baby as calm and happy as possible and want to avoid</p>
        <p class="body">clothes we have to pull over their head. I provide all clothing, hats and props at your session.</p>
      </div>
    </div>
    <div class="section" style="left:36px;top:308px;width:228px">
      <div class="section-head"><span class="num">5</span>Pacifier</div>
      <div class="cols">
        <p class="body">Please bring a pacifier. It can be very helpful during a session if a baby is fussy. Please note I only use the pacifier for a few minutes at a time to soothe into a pose. If you choose not to bring a pacifier I</p>
        <p class="body">will respect your decision, but please understand we may have to pass on several poses if you do not bring one.</p>
      </div>
    </div>
  </div>
</section>

<section class="spread spread--studio">
  <div class="page page--beige">
    <div class="section" style="left:34px;top:25px;width:230px">
      <div class="section-head">Studio</div>
      <div class="cols">
        <p class="body">My studio is kept very warm to make sure your baby is comfortable through the whole session. It will be around 75 to 80 degrees, so please dress in layers for comfort. I will have cold bottles of water available during your session. Please note, if you ask me to turn the heat down, I cannot guarantee any results for your session. Babies are used to 98.6 degrees in the</p>
        <p class="body">womb, and a cold studio will wake baby immediately. Babies do not wear much during their sessions and lose heat quickly. If you ask me to turn the heat down, and baby is fussy, I will finish the session with only swaddled poses, or with parents.</p>
      </div>
    </div>
    <div class="section" style="left:34px;top:101px;width:230px">
      <div class="section-head">Your role</div>
      <div class="cols">
        <p class="body">Your role at this session is to sit back and relax. I need very little assistance during the session, and want you to take this time to rest and enjoy the session. Feel free to nap, catch up on work, or whatever you</p>
        <p class="body">like. If baby needs to feed during the session that will be your only task! I will occasionally ask for a spotter for safety on some poses.</p>
      </div>
    </div>
    <div class="section" style="left:34px;top:159px;width:230px">
      <div class="section-head">Time</div>
      <div class="cols">
        <p class="body">Your session will last between 2 to 4 hours, please keep this in mind. I will provide bottled water and light snacks but you may want to bring more food since the session can last up to 4 hours. Please note that I cannot shoot past 4 hours, if baby is fussy I</p>
        <p class="body">will do my best to get beautiful photos. At 3 hours if baby is still fussy I will let you know that we need to switch to swaddled poses to finish the session, or we can do more family photos as well.</p>
      </div>
    </div>
    <div class="section" style="left:34px;top:225px;width:230px">
      <div class="section-head">Family photos/clothing</div>
      <div class="cols">
        <p class="body">I highly recommend mom and dad wear simple white or cream shirts, or black or navy shirts which will keep the focus on the baby. Mom can choose a tank top or dress as well. That is only a suggestion, and you are welcome to wear anything you choose. If dad is comfortable</p>
        <p class="body">baring his chest it can make for some beautiful images, but that is totally up to dad! My photos of newborns with mom and dad are generally from the waist up, so your pants or shoes will not matter.</p>
      </div>
    </div>
    <div class="section" style="left:34px;top:288px;width:230px">
      <div class="section-head">Sibling photos</div>
      <div class="cols">
        <p class="body">Photos of your newborn with their siblings are included, and will be done at the very beginning of the session. I recommend sibling boys wear cream or white tops or plain dark shirts with jeans. Sibling girls can wear cream or white shirts with jeans or dresses. I do not recommend bringing toddlers for the</p>
        <p class="body">entire session. It is very hot in my studio and there is not room for them to play, which makes them unhappy! Please plan to bring them for photos at the beginning of the session, and have a grandparent take them out while we finish.</p>
      </div>
    </div>
  </div>
  <div class="page page--coral">
    <div class="photo photo--round" role="img" aria-label="Photo of a sleeping newborn in a yellow wrap inside a wreath of coral, pink and golden flowers"
      style="left:52px;top:3px;width:196px;height:198px;background:radial-gradient(circle,#f4d46a 0%,#efb86a 28%,#e6876a 50%,#e0714f 68%,#eeaa5a 84%,#e98c7a 100%)"></div>
    <div class="script-title" style="position:absolute;left:0;top:219px;width:100%;font-size:17px;color:var(--white);line-height:1.4">What I need to know<br>before your (my) session</div>
    <div class="section" style="left:34px;top:274px;width:230px">
      <div class="cols">
        <div>
          <p class="body"><span class="num num--small">1</span> Please e-mail me with the baby's birth date, birth weight, sex, and name. Remember, my newborn sessions take place between 5 to 11 days old, so it is critical to e-mail me when baby arrives to schedule your session.</p>
          <p class="body" style="margin-top:5px"><span class="num num--small">2</span> If you have any favorite colors please feel free to let me know and I will be happy to work them into your session. Please also let me know if there are any colors you do not want used. You can create an account on my website and select a set of favorites, I will look at those before your session.</p>
        </div>
        <div>
          <p class="body"><span class="num num--small">3</span> If you have specific shots in mind for your session, or any props you have seen on my website that you would like me to use, you must let me know in advance. It takes a lot of preparation for a session, so please tell me beforehand.</p>
          <p class="body" style="margin-top:5px"><span class="num num--small">4</span> Please let me know if you have any siblings you would like to include in the session and their ages.</p>
        </div>
      </div>
    </div>
  </div>
</section>

</body>
</html>
```